Design a two-sided greeting card

Hello, I currently have a design for a greeting card (like a thank you card or business card), but I would like to improve it and make it more creative.

For the Front, I would like for you to focus most of your creativity. I like the use of just the star part of my logo. It needs to read "With love from BrightHaven!" It needs to also have a large white area (maybe not exactly white, but close to white or a gradient) where somebody could write a note.

For the Back design I generally like how it looks, but feel free to try any other ideas. It should be black or dark grey with the full logo (including the text "BrightHaven Advisors"). Underneath the logo should have our website www.brighthavenadvisors-example.com. At the very bottom should be this disclosure statement: INVESTMENT ADVICE OFFERED THROUGH BRIGHTHAVEN ADVISORS, A REGISTERED INVESTMENT ADVISOR.

Very important, the end size will be 3 1/2 x 5 inches, but please include 0.25 inches of bleed on each side that will but cut off. This means your design needs to be 4 x 5.5 inches.

I am uploading a few files:
(1) My original version as "Front" and "Back"
(2) My logo

Thank you and feel free to post any questions in the message board. Also, please do not try to contact me outside of Jobharbour as I will disqualify your entries.

```html
<!DOCTYPE html>
<html lang="en">
<head>
<meta charset="utf-8">
<title>BrightHaven Advisors – Greeting Card, Front and Back</title>
<link href="https://fonts.googleapis.com/css2?family=Dancing+Script:wght@500&family=Cinzel:wght@600&family=Cormorant+Garamond:ital,wght@1,500&family=Open+Sans:wght@400;600&display=swap" rel="stylesheet">
<style>
  :root {
    --page-bg: #b4b8bd;
    --leaf-green: #7ac143;
    --leaf-green-deep: #5fa52e;
    --paper-white: #ffffff;
    --ink: #1d1d1d;
    --charcoal: #3a3a3c;
    --charcoal-soft: #444446;
    --light-text: #e9e9e9;
  }
  * { box-sizing: border-box; margin: 0; padding: 0; }
  html, body {
    width: 835px;
    height: 1200px;
    overflow: hidden;
    background: var(--page-bg);
  }
  .sheet {
    position: relative;
    width: 835px;
    height: 1200px;
  }
  .card {
    position: absolute;
    left: 57px;
    width: 720px;
    height: 504px;
    overflow: hidden;
    box-shadow: 0 4px 14px rgba(0,0,0,0.18);
  }

  /* ---------- Front ---------- */
  .card-front {
    top: 58px;
    background: linear-gradient(180deg,
      var(--leaf-green) 0%,
      #a6d67a 28%,
      #e4f2d6 48%,
      var(--paper-white) 60%,
      var(--paper-white) 100%);
  }
  .front-greeting {
    position: absolute;
    top: 30px;
    right: 44px;
    font-family: "Dancing Script", cursive;
    font-weight: 500;
    font-size: 42px;
    color: var(--ink);
    letter-spacing: 0.5px;
  }
  .hanging-ornaments {
    position: absolute;
    top: 96px;
    left: 40px;
    width: 640px;
    height: 90px;
    background: linear-gradient(180deg, rgba(95,165,46,0.35), rgba(122,193,67,0.08));
    border-radius: 4px;
  }
  .note-text {
    position: absolute;
    top: 238px;
    left: 38px;
    width: 380px;
    font-family: "Cormorant Garamond", serif;
    font-style: italic;
    font-weight: 500;
    font-size: 16px;
    line-height: 1.35;
    color: var(--ink);
    text-align: justify;
  }
  .signature-mark {
    position: absolute;
    top: 440px;
    left: 206px;
    width: 44px;
    height: 26px;
    background: linear-gradient(90deg, #d8d8d8, #eeeeee);
    border-radius: 3px;
  }
  .corner-accent {
    position: absolute;
    right: 40px;
    bottom: -40px;
    width: 250px;
    height: 250px;
  }

  /* ---------- Back ---------- */
  .card-back {
    top: 640px;
    background: linear-gradient(160deg, var(--charcoal-soft), var(--charcoal));
    text-align: center;
  }
  .brand-dot {
    position: absolute;
    top: 70px;
    left: 50%;
    width: 96px;
    height: 96px;
    margin-left: -48px;
    border-radius: 50%;
    background: var(--leaf-green);
  }
  .brand-name {
    position: absolute;
    top: 196px;
    left: 0;
    width: 100%;
    font-family: "Cinzel", serif;
    font-weight: 600;
    font-size: 44px;
    letter-spacing: 1px;
    color: var(--leaf-green);
  }
  .brand-website {
    position: absolute;
    top: 296px;
    left: 0;
    width: 100%;
    font-family: "Open Sans", sans-serif;
    font-size: 14px;
    color: var(--light-text);
  }
  .brand-disclosure {
    position: absolute;
    top: 326px;
    left: 0;
    width: 100%;
    font-family: "Open Sans", sans-serif;
    font-size: 11.5px;
    line-height: 1.45;
    text-transform: uppercase;
    color: var(--light-text);
  }
</style>
</head>
<body>
<main class="sheet">

  <section class="card card-front" aria-label="Card front">
    <h1 class="front-greeting">With love from BrightHaven</h1>
    <div class="hanging-ornaments" role="img" aria-label="Row of small decorative hanging ornaments"></div>
    <p class="note-text">Thank you for trusting us with your goals this year. Your partnership means the world to our whole team, and we are grateful for every conversation we have shared. May the season ahead bring you calm, good health and bright new plans. We look forward to helping you build what matters most in the years to come.</p>
    <div class="signature-mark" role="img" aria-label="Handwritten initials"></div>
    <svg class="corner-accent" viewBox="0 0 250 250" role="img" aria-label="Large decorative accent in brand green">
      <defs>
        <radialGradient id="accentGlow" cx="50%" cy="50%" r="50%">
          <stop offset="0%" stop-color="#ffffff"/>
          <stop offset="55%" stop-color="#b9e08f"/>
          <stop offset="100%" stop-color="#7ac143"/>
        </radialGradient>
      </defs>
      <circle cx="125" cy="125" r="118" fill="url(#accentGlow)"/>
    </svg>
  </section>

  <section class="card card-back" aria-label="Card back">
    <div class="brand-dot" aria-hidden="true"></div>
    <h2 class="brand-name">BrightHaven Advisors</h2>
    <p class="brand-website">www.brighthavenadvisors-example.com</p>
    <p class="brand-disclosure">Investment advice offered through BrightHaven Advisors,<br>a registered investment advisor.</p>
  </section>

</main>
</body>
</html>
```